Website design needed for Renewable utilities company based in New Zealand.

Website design needed for Lanternvale Holdings based in New Zealand.

Please see attached logo.

We sell solar panels, vertical axis wind turbines, atmospheric water generators and other related equipment for those who don't have access or don't want to depend on the government, city councils for their utilities (power and water).

We like metallic texture, dark grey and purple, red or blue colours. The design should go well with the attached logo.

Target Market(s)

The Eco conscious

Industry/Entity Type

Government

Logo Text

Lanternvale Summit

Requirements
Must have
• Must Have:
- Metallic finish is a must.
- Design should fit around the attached logo well.
Nice to have
• Sharpe design prefred rather than rounded edges

```html
<!DOCTYPE html>
<html lang="en">
<head>
<meta charset="utf-8">
<title>Lanternvale Summit</title>
<link href="https://fonts.googleapis.com/css2?family=Open+Sans:wght@400;600;700&display=swap" rel="stylesheet">
<style>
:root{
  --bg:#2e2e2e;
  --page:#ffffff;
  --navy:#0b2a8f;
  --nav:#0a3d9c;
  --sky:#1a9fe0;
  --text:#555555;
  --dark:#333333;
  --footer:#0b0b0b;
  --grey-btn:#5e5e5e;
}
*{box-sizing:border-box;margin:0;padding:0}
html,body{width:750px;height:1200px;overflow:hidden}
body{background:var(--bg);font-family:"Open Sans",Arial,sans-serif;color:var(--text);position:relative}
.page{position:absolute;left:78px;top:10px;width:592px;height:1164px;background:var(--page)}
.abs{position:absolute}
.brand{left:20px;top:72px;display:flex;align-items:center;gap:6px;font-size:17px;color:var(--sky);font-weight:400}
.brand-mark{position:absolute;left:60px;top:18px;width:44px;height:44px;border-radius:50%;background:var(--navy)}
.social{left:474px;top:32px;display:flex;gap:4.5px}
.social span{width:18px;height:18px;background:#3b5a8f}
.nav{left:186px;top:71px;height:26px;display:flex;background:var(--nav)}
.nav a{display:flex;align-items:center;justify-content:center;color:#fff;font-size:9.5px;text-decoration:none;border-right:1px solid #0a2f7a}
.nav a.active{background:var(--sky)}
.hero{left:0;top:97px;width:592px;height:209px;background:linear-gradient(180deg,#1e6fc4 0%,#4aa3e6 55%,#bcdcf3 72%,#1b3f88 78%,#2c5aa8 100%)}
.hero-title{left:288px;top:122px;font-size:38px;font-weight:700;color:#fff;letter-spacing:.5px}
.hero-text{left:290px;top:175px;width:235px;font-size:11.5px;line-height:14px;color:#d8ecff}
.btn-navy{left:290px;top:241px;width:65px;height:21px;background:var(--navy);color:#fff;font-size:6.5px;display:flex;align-items:center;justify-content:center}
.hero-arrow{top:190px}
.shadow{left:15px;width:562px;height:10px;background:radial-gradient(ellipse at top,rgba(0,0,0,.18),rgba(0,0,0,0) 70%)}
.welcome-title{left:0;top:332px;width:592px;text-align:center;font-size:19px;color:var(--dark)}
.welcome-text{left:0;top:362px;width:592px;text-align:center;font-size:8.5px;line-height:13px;color:var(--dark)}
.why-title{left:13px;top:436px;font-size:18.5px;color:#111}
.why-title em{font-style:normal;color:var(--sky)}
.why-title b{font-weight:400;color:var(--navy)}
.why-text{left:13px;width:340px;font-size:9px;line-height:11px;color:#666}
.why-list{left:44px;top:560px;font-size:9px;line-height:12px;color:#666;list-style:square}
.inquiry{left:383px;top:434px;width:198px;height:194px;background:linear-gradient(180deg,#f4f4f4,#e6e6e6);border:1px solid #cfcfcf;box-shadow:0 1px 4px rgba(0,0,0,.25)}
.inquiry-head{height:34px;background:linear-gradient(180deg,#9a9a9a,#5c5c5c);color:#fff;font-size:18px;display:flex;align-items:center;justify-content:center}
.field{position:absolute;left:28px;width:143px;height:17px;background:#fff;border:1px solid #d6d6d6;font-size:8px;color:#777;padding:3px 5px}
.submit{position:absolute;left:61px;top:154px;width:83px;height:24px;background:linear-gradient(180deg,#1a3fc0,#061f7a);color:#fff;font-weight:700;font-size:10px;display:flex;align-items:center;justify-content:center}
.products-title{left:0;top:676px;width:592px;text-align:center;font-size:18.5px;color:var(--sky)}
.card{top:714px;width:153px;height:229px;background:#efefef}
.card-img{width:153px;height:121px}
.card h3{margin-top:14px;text-align:center;font-size:11.5px;font-weight:600;color:var(--navy)}
.card p{margin-top:4px;text-align:center;font-size:8.5px;line-height:12.5px;color:#444;padding:0 10px}
.card .more{margin:7px auto 0;width:59px;height:18px;background:var(--grey-btn);color:#fff;font-size:7.5px;display:flex;align-items:center;justify-content:center;box-shadow:0 1px 2px rgba(0,0,0,.4)}
.chev{top:818px;font-size:28px;color:#111}
.footer{left:0;top:968px;width:592px;height:196px;background:var(--footer)}
.f-head{top:30px;font-size:12.5px;color:var(--sky)}
.f-links{left:12px;top:59px;list-style:none;font-size:8px;line-height:13.2px;color:#fff}
.f-links li:first-child{color:var(--sky)}
.f-text{font-size:7.5px;line-height:11.4px;color:#fff}
.f-input{background:#fff;font-size:7.5px;color:#222;padding:4px 5px}
.f-btn{background:var(--sky);color:#fff;display:flex;align-items:center;justify-content:center}
.contact-row{left:474px;display:flex;gap:8px;font-size:7.5px;line-height:13.5px;color:#fff}
.contact-row svg{flex:none;margin-top:2px}
.copyright{left:0;top:1178px;width:750px;text-align:center;font-size:6.5px;color:#999}
</style>
</head>
<body>
<div class="page">
  <header>
    <div class="abs brand-mark"></div>
    <div class="abs brand">Lanternvale Summit</div>
    <div class="abs social" aria-label="Social links"><span></span><span></span><span></span><span></span><span></span></div>
    <nav class="abs nav">
      <a class="active" style="width:53px">Home</a>
      <a style="width:66px">About us</a>
      <a style="width:84px">Our Products</a>
      <a style="width:50px">News</a>
      <a style="width:74px">Get a Quote</a>
      <a style="width:80px;border-right:0">Contact Us</a>
    </nav>
  </header>

  <section>
    <div class="abs hero" role="img" aria-label="Wind turbines against a blue sky above rows of solar panels"></div>
    <div class="abs hero-title">TURBINES</div>
    <p class="abs hero-text">Lorem ipsum dolor sit amet, consectetur adipisicing elit, sed do eiusmod tempor incididunt ut labore et dolore magna aliqua.</p>
    <div class="abs btn-navy">Read More</div>
    <svg class="abs hero-arrow" style="left:13px" width="20" height="20" viewBox="0 0 20 20"><circle cx="10" cy="10" r="9.5" fill="#fff"/><path d="M12 5 7 10l5 5" stroke="#1b5bb5" stroke-width="2.4" fill="none"/></svg>
    <svg class="abs hero-arrow" style="left:561px" width="20" height="20" viewBox="0 0 20 20"><circle cx="10" cy="10" r="9.5" fill="#fff"/><path d="M8 5l5 5-5 5" stroke="#1b5bb5" stroke-width="2.4" fill="none"/></svg>
    <div class="abs shadow" style="top:306px"></div>
  </section>

  <section>
    <h1 class="abs welcome-title" style="font-weight:400">Welcome to our website</h1>
    <p class="abs welcome-text">Lorem ipsum dolor sit amet, consectetur adipisicing elit, sed do eiusmod tempor incididunt ut labore et dolore magna aliqua.<br>Ut enim ad minim veniam, quis nostrud exercitation ullamco laboris nisi ut aliquip ex ea commodo</p>
    <div class="abs shadow" style="top:408px"></div>
  </section>

  <section>
    <h2 class="abs why-title" style="font-weight:400">Why <em>Lanternvale</em> <b>Summit</b></h2>
    <p class="abs why-text" style="top:471px">Lorem ipsum dolor sit amet, consectetur adipisicing elit, sed do eiusmod tempor incididunt ut labore et dolore magna aliqua. Ut enim ad minim veniam, quis</p>
    <p class="abs why-text" style="top:504px">Duis aute irure dolor in reprehenderit in voluptate velit esse cillum dolore eu fugiat nulla pariatur. Excepteur sint occaecat cupidatat non proident, sunt in culpa qui officia deserunt mollit anim id est laborum Lorem ipsum dolor sit amet, consectetur adipisicing elit, sed do eiusmod.</p>
    <ul class="abs why-list">
      <li>Adipisicing elit</li><li>Eiusmod tempor</li><li>Incididunt ut</li><li>labore et Dolore</li><li>magna aliqua.</li>
    </ul>
    <form class="abs inquiry">
      <div class="inquiry-head">Quick Inquiry</div>
      <div class="field" style="top:49px">Name</div>
      <div class="field" style="top:75px">Email Address</div>
      <div class="field" style="top:103px;height:36px">Message</div>
      <div class="submit">Submit</div>
    </form>
    <div class="abs shadow" style="top:658px"></div>
  </section>

  <section>
    <h2 class="abs products-title" style="font-weight:400">Products</h2>
    <div class="abs chev" style="left:20px">&#x2039;</div>
    <div class="abs chev" style="left:562px">&#x203A;</div>
    <article class="abs card" style="left:42px">
      <div class="card-img" role="img" aria-label="Wind turbines on a green hill" style="background:linear-gradient(180deg,#3f86d6,#a9d2f2 55%,#6fb63a 62%,#3e8a1f)"></div>
      <h3>Turbines</h3>
      <p>Lorem ipsum dolor sit amet, consectetur adipisicing elit, sed do dolore magna aliqua.</p>
      <div class="more">Read more</div>
    </article>
    <article class="abs card" style="left:221px">
      <div class="card-img" role="img" aria-label="Atmospheric water generator unit on a lawn" style="background:linear-gradient(180deg,#e6ebef,#b9c0c4 45%,#5d7a3a 70%,#4a7a2a)"></div>
      <h3>Water Generators</h3>
      <p>Lorem ipsum dolor sit amet, consectetur adipisicing elit, sed do dolore magna aliqua.</p>
      <div class="more">Read more</div>
    </article>
    <article class="abs card" style="left:398px">
      <div class="card-img" role="img" aria-label="Solar panel field below mountains" style="background:linear-gradient(180deg,#4b86c8,#9fb6c8 35%,#7a6a5a 45%,#1d4f9a 60%,#2f6fc0)"></div>
      <h3>Solar Panels</h3>
      <p>Lorem ipsum dolor sit amet, consectetur adipisicing elit, sed do dolore magna aliqua.</p>
      <div class="more">Read more</div>
    </article>
  </section>

  <footer class="abs footer">
    <h4 class="abs f-head" style="left:12px;font-weight:400">Navigation</h4>
    <ul class="abs f-links"><li>Home</li><li>About us</li><li>Our Products</li><li>News</li><li>Get a Quote</li><li>Contact Us</li></ul>

    <h4 class="abs f-head" style="left:125px;font-weight:400">Newsletter Sign up</h4>
    <p class="abs f-text" style="left:125px;top:58px;width:125px">Lorem ipsum dolor sit amet, consectetur adipisicing elit, sed do eiusmod tempor incididunt ut labore et dolore magna aliqua. Ut</p>
    <div class="abs f-input" style="left:126px;top:109px;width:93px;height:19px">Email address</div>
    <div class="abs f-btn" style="left:219px;top:109px;width:29px;height:19px;font-size:7.5px">Join</div>
    <p class="abs f-text" style="left:125px;top:133px;font-size:6.5px">We respect your privacy</p>

    <h4 class="abs f-head" style="left:307px;font-weight:400">Quick Contact</h4>
    <div class="abs f-input" style="left:308px;top:56px;width:118px;height:20px">Name</div>
    <div class="abs f-input" style="left:308px;top:80px;width:118px;height:19px">E-mail</div>
    <div class="abs f-input" style="left:308px;top:104px;width:118px;height:40px">Message</div>
    <div class="abs f-btn" style="left:308px;top:150px;width:59px;height:20px;font-size:9px;font-weight:600">Submit</div>

    <h4 class="abs f-head" style="left:476px;font-weight:400">Contact US</h4>
    <div class="abs contact-row" style="top:64px">
      <svg width="9" height="7" viewBox="0 0 9 7"><rect width="9" height="7" fill="#888"/><path d="M0 0l4.5 4L9 0" stroke="#0b0b0b" fill="none"/></svg>
      <span style="font-weight:600">hello@lanternvale.example</span>
    </div>
    <div class="abs contact-row" style="top:84px">
      <svg width="9" height="9" viewBox="0 0 9 9"><path d="M2 0l2 2-1 1.5c.6 1.2 1.3 1.9 2.5 2.5L7 5l2 2-1.5 2C4 8.5.5 5 0 1.5z" fill="#888"/></svg>
      <span>P: +64 9 555 0142<br>F: +64 9 555 0143</span>
    </div>
    <div class="abs contact-row" style="top:120px">
      <svg width="9" height="11" viewBox="0 0 9 11"><path d="M4.5 0A4.5 4.5 0 0 0 0 4.5C0 7.5 4.5 11 4.5 11S9 7.5 9 4.5A4.5 4.5 0 0 0 4.5 0z" fill="#888"/><circle cx="4.5" cy="4.5" r="1.6" fill="#0b0b0b"/></svg>
      <span>14 Kowhai Lane, Suite 3<br>Auckland, New Zealand 1010</span>
    </div>
  </footer>
</div>
<p class="abs copyright">Copyright &copy; 2013 Lanternvale Summit.</p>
</body>
</html>
```